Brimovex business card

Based on company logo and website given , to design a business card temple. Slogan "Your furry friends deserves the best"
Color style please refer to our website

```html
<!DOCTYPE html>
<html lang="en">
<head>
<meta charset="utf-8">
<title>Brimovex business card</title>
<link href="https://fonts.googleapis.com/css2?family=Montserrat:wght@400;500;600;700&display=swap" rel="stylesheet">
<style>
  :root {
    --olive: #b8ad24;
    --olive-shade: #9e9420;
    --paper: #ffffff;
    --ink: #3b3b3b;
    --muted: #6d6d6d;
    --backdrop: #e6e6e4;
  }
  * { margin: 0; padding: 0; box-sizing: border-box; }
  html, body {
    width: 1200px;
    height: 675px;
    overflow: hidden;
    background: var(--backdrop);
    font-family: "Montserrat", sans-serif;
  }
  .canvas {
    position: relative;
    width: 1200px;
    height: 675px;
  }
  .card {
    position: absolute;
    top: 194px;
    width: 500px;
    height: 286px;
    border-radius: 16px;
    overflow: hidden;
    box-shadow: 0 10px 28px rgba(0,0,0,0.14);
  }

  /* Front */
  .card-front {
    left: 60px;
    background: var(--olive);
  }
  .front-decoration {
    position: absolute;
    left: 0;
    top: 0;
    width: 230px;
    height: 286px;
    background: linear-gradient(135deg, var(--olive-shade) 0%, var(--olive) 85%);
    border-top-right-radius: 120px;
    opacity: 0.6;
  }
  .front-wordmark {
    position: absolute;
    left: 200px;
    top: 118px;
    color: var(--paper);
    font-weight: 600;
    font-size: 44px;
    line-height: 1;
    letter-spacing: 0.5px;
  }

  /* Back */
  .card-back {
    left: 640px;
    background: var(--paper);
  }
  .holder {
    position: absolute;
    left: 34px;
    top: 36px;
  }
  .holder-name {
    color: var(--olive);
    font-weight: 700;
    font-size: 22px;
    letter-spacing: 1px;
    line-height: 1;
  }
  .holder-role {
    color: var(--muted);
    font-size: 10px;
    margin-top: 4px;
  }
  .back-wordmark {
    position: absolute;
    right: 40px;
    top: 62px;
    color: var(--olive);
    font-weight: 600;
    font-size: 36px;
    line-height: 1;
  }
  .back-rule {
    position: absolute;
    left: 34px;
    right: 34px;
    top: 118px;
    height: 1.5px;
    background: var(--olive);
  }
  .contacts {
    position: absolute;
    left: 34px;
    top: 140px;
    display: flex;
    gap: 30px;
  }
  .contact-column {
    display: flex;
    flex-direction: column;
    gap: 10px;
  }
  .contact-item {
    display: flex;
    align-items: center;
    gap: 7px;
    color: var(--ink);
    font-size: 11px;
    font-weight: 500;
    white-space: nowrap;
  }
  .contact-icon {
    width: 13px;
    height: 13px;
    flex: none;
  }
</style>
</head>
<body>
<main class="canvas">

  <section class="card card-front" aria-label="Card front">
    <div class="front-decoration" role="img" aria-label="Large outline of a dog and cat in a darker olive tone"></div>
    <div class="front-wordmark">Brimovex</div>
  </section>

  <section class="card card-back" aria-label="Card back">
    <div class="holder">
      <div class="holder-name">NAME</div>
      <div class="holder-role">Owner</div>
    </div>

    <div class="back-wordmark">Brimovex</div>
    <div class="back-rule"></div>

    <div class="contacts">
      <div class="contact-column">
        <div class="contact-item">
          <svg class="contact-icon" viewBox="0 0 13 13"><rect width="13" height="13" rx="2" fill="#b8ad24"/><rect x="3" y="4" width="7" height="5" fill="none" stroke="#fff" stroke-width="1"/><path d="M3 4 L6.5 7 L10 4" fill="none" stroke="#fff" stroke-width="1"/></svg>
          <span>hello@brimovex.com</span>
        </div>
      </div>
      <div class="contact-column">
        <div class="contact-item">
          <svg class="contact-icon" viewBox="0 0 13 13"><rect width="13" height="13" rx="2" fill="#b8ad24"/><path d="M6.5 10.5 C4.5 8 4 7 4 5.8 A2.5 2.5 0 0 1 9 5.8 C9 7 8.5 8 6.5 10.5Z" fill="#fff"/><circle cx="6.5" cy="5.8" r="0.9" fill="#b8ad24"/></svg>
          <span>Address, City, state zip Code.</span>
        </div>
        <div class="contact-item">
          <svg class="contact-icon" viewBox="0 0 13 13"><rect width="13" height="13" rx="2" fill="#b8ad24"/><path d="M4 3.5 L5.5 3.5 L6 5.5 L5 6.2 C5.5 7.3 6 7.8 7 8.2 L7.7 7.2 L9.5 7.7 L9.5 9.2 C6.5 9.5 3.7 6.8 4 3.5Z" fill="#fff"/></svg>
          <span>Calling Number</span>
        </div>
        <div class="contact-item">
          <svg class="contact-icon" viewBox="0 0 13 13"><rect width="13" height="13" rx="2" fill="#b8ad24"/><circle cx="6.5" cy="6.5" r="3.2" fill="none" stroke="#fff" stroke-width="0.9"/><path d="M3.3 6.5 H9.7 M6.5 3.3 C5 5 5 8 6.5 9.7 M6.5 3.3 C8 5 8 8 6.5 9.7" fill="none" stroke="#fff" stroke-width="0.8"/></svg>
          <span>www.brimovex.com</span>
        </div>
      </div>
    </div>
  </section>

</main>
</body>
</html>
```